Heron Accord Business Card

Need a business card for my nonprofit, Heron Accord Inc. Heron Accord is a conflict resolution practice that offers services that help people resolve problems peacefully.

Got Conflict? Try Conflict Coaching. Initial consultation is complimentary

Marisol Daventry-Kuhl, PhD
Heron Accord Inc.
www.heronaccord-example.org
E: info@heronaccord-example.org
P: 555-318-4927

Would like the attached logo on it, as well as our slogan, which is Finding Calm Around the RoomĀ®

```html
<!DOCTYPE html>
<html lang="en">
<head>
<meta charset="UTF-8">
<title>Heron Accord Business Card</title>
<link rel="stylesheet" href="https://fonts.googleapis.com/css2?family=Montserrat:wght@400;500;600&display=swap">
<style>
  :root {
    --bg: #ecebe8;
    --red: #ec1f2b;
    --red-soft: #f2545a;
    --gold: #b89a5e;
    --blush: #f8ddd3;
    --paper: #ffffff;
    --ink-shadow: rgba(40, 30, 20, 0.18);
  }
  * { box-sizing: border-box; margin: 0; padding: 0; }
  html, body {
    width: 1200px; height: 900px; overflow: hidden;
    background: var(--bg);
    font-family: "Montserrat", Arial, sans-serif;
  }
  .canvas {
    width: 1200px; height: 900px;
    display: flex; flex-direction: column;
    align-items: center; justify-content: center; gap: 56px;
  }
  .card {
    position: relative; width: 620px; height: 354px;
    box-shadow: 0 10px 28px var(--ink-shadow);
    overflow: hidden;
  }
  /* Front */
  .card-front {
    background: linear-gradient(120deg, var(--red) 0%, var(--red) 55%, var(--red-soft) 100%);
    display: flex; align-items: center; justify-content: center;
  }
  .front-mark {
    position: absolute; width: 300px; height: 300px; border-radius: 50%;
    background: rgba(255, 255, 255, 0.14);
    left: 50%; top: 50%; transform: translate(-50%, -50%);
  }
  .front-name {
    position: relative; display: flex; align-items: center; gap: 14px;
    color: #e9cf94; font-weight: 600; font-size: 46px; letter-spacing: 4px;
    text-transform: uppercase;
  }
  .dot { width: 18px; height: 18px; border-radius: 50%; background: currentColor; }
  /* Back */
  .card-back { background: var(--paper); color: var(--gold); }
  .back-mark {
    position: absolute; width: 230px; height: 230px; border-radius: 50%;
    background: var(--blush); opacity: 0.75;
    left: 50%; top: 52%; transform: translate(-50%, -50%);
  }
  .brand {
    position: absolute; left: 30px; top: 26px;
    display: flex; align-items: center; gap: 8px;
    font-weight: 600; font-size: 25px; letter-spacing: 2px; text-transform: uppercase;
  }
  .brand .dot { width: 10px; height: 10px; }
  .contact {
    position: absolute; left: 30px; top: 76px; list-style: none;
    font-size: 12px; line-height: 18px;
  }
  .contact li { display: flex; align-items: center; gap: 7px; }
  .contact svg { width: 11px; height: 11px; fill: var(--red); }
  .rule { position: absolute; height: 1.5px; background: var(--red); }
  .rule-top { left: 30px; top: 118px; width: 330px; }
  .rule-bottom { left: 30px; right: 30px; top: 262px; }
  .person {
    position: absolute; right: 34px; top: 138px;
    font-weight: 600; font-size: 17px;
  }
  .person .title { color: var(--red); }
  .org { position: absolute; right: 34px; top: 208px; text-align: right; font-weight: 600; font-size: 14px; line-height: 19px; }
  .org .org-name { color: var(--red); }
  .slogan { position: absolute; left: 0; right: 0; top: 274px; text-align: center; font-weight: 600; font-size: 16px; }
  .offer { position: absolute; left: 0; right: 0; top: 304px; text-align: center; font-weight: 500; font-size: 13px; }
</style>
</head>
<body>
<main class="canvas">
  <section class="card card-front" aria-label="Card front">
    <div class="front-mark"></div>
    <div class="front-name"><span class="dot"></span>Heron Accord</div>
  </section>

  <section class="card card-back" aria-label="Card back">
    <div class="back-mark"></div>
    <div class="brand"><span class="dot"></span>Heron Accord</div>
    <ul class="contact">
      <li><svg viewBox="0 0 12 12"><rect x="3" y="0.5" width="6" height="11" rx="1.2"/></svg>555-318-4927</li>
      <li><svg viewBox="0 0 12 12"><path d="M0 2h12v8H0z M1 3l5 4 5-4" /></svg>info@heronaccord-example.org</li>
    </ul>
    <div class="rule rule-top"></div>
    <p class="person">Marisol Daventry-Kuhl, <span class="title">PhD</span></p>
    <p class="org"><span class="org-name">Heron Accord Inc.</span><br>www.heronaccord-example.org</p>
    <div class="rule rule-bottom"></div>
    <p class="slogan">Finding Calm Around the Room®</p>
    <p class="offer">Got Conflict? Try Conflict Coaching. Initial consultation is complimentary.</p>
  </section>
</main>
</body>
</html>
```